Prayer Service 12.28.2013

I need a flyer designed for a Christian prayer service. The title and theme is:
"Total and Complete Surrender for Total and Complete Deliverance!"
1. You have creative freedom with imagery and typography
2. I need a quick turnaround time
FLYER DETAILS:
A prayer, anointing, and deliverance all night prayer service, at Brookhaven Assembly.
Saturday December 28 2013 from 9pm-6am.
Special guest speakers, prayer,anointing,and deliverance sessions.
For more information contact Sis Mirela Thornbury at Brookhaven Assembly 347 562 1094 Ext. 4816 or Janelle Corbin at 631 538-2904

```html
<!DOCTYPE html>
<html lang="en">
<head>
<meta charset="utf-8">
<title>Prayer Service Flyer</title>
<link href="https://fonts.googleapis.com/css2?family=Roboto+Condensed:wght@400;700;900&family=Roboto:wght@400;500&family=Tinos:wght@400&display=swap" rel="stylesheet">
<style>
  :root {
    --canvas: #e9e4dc;
    --paper: #ffffff;
    --sun: #f6b928;
    --amber: #c98a1c;
    --bronze: #7a4f18;
    --umber: #3b2a20;
    --night: #2a1e18;
    --gold-text: #f3b233;
    --white-text: #ffffff;
    --rule: #d9d2c8;
  }
  * { margin: 0; padding: 0; box-sizing: border-box; }
  html, body { width: 1200px; height: 1000px; overflow: hidden; background: var(--canvas); }
  .flyer {
    position: absolute; left: 320px; top: 40px;
    width: 560px; height: 920px;
    background: var(--paper);
    padding: 14px;
    box-shadow: 0 6px 24px rgba(0,0,0,.18);
  }
  .artwork {
    position: relative; width: 100%; height: 100%; overflow: hidden;
    background: linear-gradient(180deg, var(--sun) 0%, var(--amber) 14%, var(--bronze) 28%, var(--umber) 44%, var(--night) 100%);
  }
  .hands-photo {
    position: absolute; left: 0; top: 300px; width: 300px; height: 520px;
    background: radial-gradient(ellipse at 45% 40%, #c9a06a 0%, #8d6438 40%, rgba(59,42,32,0) 75%);
  }
  .date-block { position: absolute; right: 22px; top: 30px; text-align: right; }
  .day {
    font-family: "Roboto Condensed", sans-serif; font-weight: 900;
    font-size: 92px; line-height: .95; color: var(--gold-text); letter-spacing: -1px;
  }
  .date, .time {
    font-family: "Roboto Condensed", sans-serif; font-weight: 700;
    font-size: 34px; line-height: 1.15; color: var(--white-text);
  }
  .title {
    position: absolute; left: 20px; right: 16px; top: 232px;
    font-family: "Tinos", serif; font-size: 34px; line-height: 1.08;
    color: var(--gold-text);
  }
  .description {
    position: absolute; right: 22px; top: 340px; text-align: right;
    font-family: "Roboto", sans-serif; font-size: 23px; line-height: 1.2;
    letter-spacing: 2px; color: var(--white-text);
  }
  .rule { position: absolute; right: 22px; height: 2px; width: 270px; background: var(--rule); }
  .rule-one { top: 520px; }
  .rule-two { top: 700px; }
  .sessions {
    position: absolute; right: 22px; top: 540px; text-align: right;
    font-family: "Roboto Condensed", sans-serif; font-weight: 700;
    font-size: 33px; line-height: 1.08; color: var(--gold-text);
  }
  .contact {
    position: absolute; right: 22px; top: 716px; text-align: right;
    font-family: "Roboto Condensed", sans-serif; font-weight: 400;
    font-size: 20px; line-height: 1.35; color: var(--white-text);
  }
</style>
</head>
<body>
  <main class="flyer">
    <section class="artwork">
      <div class="hands-photo" role="img" aria-label="Photograph of clasped hands in prayer, warm sepia tones"></div>

      <div class="date-block">
        <p class="day">SATURDAY</p>
        <p class="date">December 28 2013</p>
        <p class="time">from 9pm-6am</p>
      </div>

      <h1 class="title">Total and Complete Surrender for<br>Total and Complete Deliverance!</h1>

      <p class="description">A prayer, anointing,<br>and deliverance all<br>night prayer service,<br>at Brookhaven<br>Assembly</p>

      <div class="rule rule-one"></div>
      <p class="sessions">Special guest speakers,<br>prayer, anointing, and<br>deliverance sessions</p>
      <div class="rule rule-two"></div>

      <p class="contact">For more information contact<br>Sis Mirela Thornbury at Brookhaven<br>Assembly 347 562 1094 Ext. 4816<br>or Janelle Corbin at 631 538-2904</p>
    </section>
  </main>
</body>
</html>
```